MSA Plans

I would like to rebuild my brochure for the 3 business plans that I currently offer my clients. I would like to make it look much more modern & attractive to clients when choosing one of our service plans. If we can stick to a tech theme that would be great. Message me for anymore information.

```html
<!DOCTYPE html>
<html lang="en">
<head>
<meta charset="utf-8">
<title>Managed Services Framework</title>
<link href="https://fonts.googleapis.com/css2?family=Syncopate:wght@700&family=Barlow:ital,wght@0,400;0,600;1,400&family=Barlow+Condensed:wght@400;500;600;700&display=swap" rel="stylesheet">
<style>
  :root{
    --page:#e4e4e4;
    --paper:#ffffff;
    --orange:#f26a21;
    --orange-mid:#f59a62;
    --orange-light:#fcd9c3;
    --amber:#f9a83a;
    --charcoal:#3a3a3a;
    --rail-dark:#333333;
    --rail-mid:#4a4a4a;
    --row-grey:#f3f3f3;
    --rule:#f3c2a6;
    --ink:#2b2b2b;
    --tick:#7cbb2e;
    --cross:#e2231a;
    --hero-dark:#3a312d;
    --hero-warm:#9a7560;
  }
  *{box-sizing:border-box;margin:0;padding:0}
  html,body{width:1200px;height:1200px;overflow:hidden;background:var(--page)}
  body{position:relative;font-family:"Barlow",Arial,sans-serif;color:var(--ink)}

  .flyer{position:absolute;left:257px;top:115px;width:686px;height:970px;background:var(--paper);overflow:hidden;box-shadow:0 6px 18px rgba(0,0,0,.18)}
  .hero-art{position:absolute;left:0;top:0;width:686px;height:540px}

  .title{position:absolute;left:52px;top:32px;font-family:"Syncopate",Arial,sans-serif;font-weight:700;font-size:29px;line-height:36px;color:#fff;letter-spacing:.5px;text-shadow:0 2px 4px rgba(0,0,0,.35)}
  .subtitle{position:absolute;left:49px;top:145px;font-style:italic;font-size:22px;line-height:28px;color:#fff;text-shadow:0 1px 3px rgba(0,0,0,.4)}

  .brand{position:absolute;left:486px;top:122px;display:flex;align-items:center;gap:8px}
  .brand-dot{width:22px;height:22px;border-radius:50%;background:var(--orange)}
  .brand-name{font-family:"Barlow Condensed",Arial,sans-serif;font-weight:700;font-size:38px;color:#fff;letter-spacing:1px}

  .agreement{position:absolute;left:65px;top:224px;width:555px}
  .agreement-head{height:38px;background:var(--orange);border-radius:8px 8px 0 0;display:flex;align-items:center;position:relative}
  .agreement-title{font-family:"Barlow Condensed",Arial,sans-serif;font-weight:700;font-size:22px;color:#fff;margin-left:56px;width:277px}
  .plan-name{position:absolute;top:11px;width:80px;text-align:center;font-family:"Barlow Condensed",Arial,sans-serif;font-size:14px;color:#fff}
  .plan-name::after{content:"";position:absolute;left:36px;top:27px;border:5px solid transparent;border-top-color:var(--orange)}

  .section{display:flex;position:relative}
  .section-rail{width:39px;flex:none;border-radius:10px 0 0 10px;display:flex;align-items:center;justify-content:center;background:var(--rail-mid)}
  .section-rail span{transform:rotate(-90deg);white-space:nowrap;font-family:"Barlow Condensed",Arial,sans-serif;font-size:15px;color:#fff;letter-spacing:.5px}
  .section.service .section-rail{background:var(--rail-dark)}
  .section.service .section-rows,.section.training .section-rows{background:var(--row-grey)}
  .section.management .section-rows,.section.support .section-rows{background:#fff}
  .section + .section{margin-top:3px}
  .section-rows{flex:1;padding:4px 16px 2px 17px}
  .section.training .section-rows{border-radius:0 0 10px 0;box-shadow:0 3px 6px rgba(0,0,0,.12)}

  .row{display:grid;grid-template-columns:277px 62px 62px 62px;column-gap:6px;height:24px;align-items:end}
  .row > div{height:100%;display:flex;align-items:center;border-bottom:1px solid var(--rule)}
  .row:last-child > div{border-bottom-color:transparent}
  .feature{font-size:12.5px;letter-spacing:.2px;color:var(--ink);white-space:nowrap}
  .cell{justify-content:center;font-family:"Barlow",Arial,sans-serif;font-weight:600;font-size:9.5px;color:var(--ink);padding-top:5px;white-space:nowrap}
  .cell svg{width:15px;height:13px}
  .cell.mark{padding-top:0}

  .price-band{position:absolute;right:66px;height:25px;display:flex;align-items:center}
  .price-band.rrp{top:801px;left:140px;background:var(--orange-light);clip-path:polygon(0 0,100% 0,100% 100%,18px 100%)}
  .price-band.users{top:827px;left:177px;background:var(--orange-mid);clip-path:polygon(0 0,100% 0,100% 100%,22px 100%)}
  .price-band.commit{top:853px;left:218px;background:var(--orange);clip-path:polygon(0 0,100% 0,100% 100%,22px 100%);color:#fff}
  .band-label{position:absolute;right:222px;font-family:"Barlow Condensed",Arial,sans-serif;font-weight:600;font-size:14px;white-space:nowrap}
  .band-value{position:absolute;width:60px;margin-left:-30px;text-align:center;font-family:"Barlow Condensed",Arial,sans-serif;font-weight:600;font-size:14px}
  .rrp .band-label,.rrp .band-value{color:var(--ink)}
  .users .band-label,.users .band-value{color:#3a2a20}

  .version{position:absolute;left:65px;top:852px;font-size:10px;line-height:16px;color:#333}

  .footer{position:absolute;left:0;top:900px;width:686px;height:70px}
  .footer-art{position:absolute;left:0;top:0}
  .footer-contact{position:absolute;left:24px;top:11px;font-family:"Barlow Condensed",Arial,sans-serif;font-size:11.5px;color:#fff;line-height:21px}
  .footer-contact div{display:flex;align-items:center;gap:7px}
  .footer-contact svg{width:10px;height:8px}
  .company{position:absolute;left:230px;width:226px;top:-2px;text-align:center;font-family:"Barlow Condensed",Arial,sans-serif;font-weight:600;font-size:17.5px;line-height:21px;color:var(--orange)}
  .abn{position:absolute;left:230px;width:226px;top:40px;text-align:center;font-family:"Barlow Condensed",Arial,sans-serif;font-size:17px;color:#fff}
  .footer-call{position:absolute;right:20px;top:7px;text-align:right;font-family:"Barlow Condensed",Arial,sans-serif;color:#fff}
  .phone{font-weight:600;font-size:20px;display:flex;align-items:center;justify-content:flex-end;gap:8px}
  .address{font-size:11.5px;margin-top:3px;display:flex;align-items:center;justify-content:flex-end;gap:9px}
  .footer-call svg{width:11px;height:12px}
</style>
</head>
<body>
<svg width="0" height="0" style="position:absolute">
  <defs>
    <symbol id="tick" viewBox="0 0 16 14"><path d="M1.5 8.2 L5.6 12 L14.6 1.6 L12.8 1 L5.6 9 L3 6.6 Z" fill="var(--tick)"/></symbol>
    <symbol id="cross" viewBox="0 0 16 14"><path d="M3 1.5 L8 5.6 L13 1.5 L14.5 2.8 L9.6 7 L14.5 11.2 L13 12.5 L8 8.4 L3 12.5 L1.5 11.2 L6.4 7 L1.5 2.8 Z" fill="var(--cross)"/></symbol>
  </defs>
</svg>

<main class="flyer">
  <svg class="hero-art" viewBox="0 0 686 540" aria-hidden="true">
    <defs>
      <linearGradient id="heroTone" x1="0" y1="0" x2="1" y2="0.6">
        <stop offset="0" stop-color="var(--hero-dark)"/>
        <stop offset="0.55" stop-color="#6e5646"/>
        <stop offset="1" stop-color="var(--hero-warm)"/>
      </linearGradient>
      <linearGradient id="amberTone" x1="0" y1="0" x2="0" y2="1">
        <stop offset="0" stop-color="var(--amber)"/>
        <stop offset="1" stop-color="#f7b547"/>
      </linearGradient>
    </defs>
    <path d="M0 268 Q40 282 72 300 L72 386 Q30 386 0 383 Z" fill="var(--orange)"/>
    <path d="M620 432 Q655 428 686 418 L686 533 Q650 505 620 482 Z" fill="url(#amberTone)"/>
  </svg>
  <svg class="hero-art" viewBox="0 0 686 540" role="img" aria-label="Photo of a hand using a laptop with glowing padlock and server security icons">
    <path d="M0 0 H686 V418 Q655 426 620 432 L620 300 Q300 300 72 300 Q40 282 0 268 Z" fill="url(#heroTone)"/>
  </svg>

  <h1 class="title">MANAGED<br>SERVICES<br>FRAMEWORK</h1>
  <p class="subtitle">Defining our services and how we<br>deliver these consistently to you.</p>

  <div class="brand"><span class="brand-dot"></span><span class="brand-name">NEXWAVE</span></div>

  <section class="agreement">
    <header class="agreement-head">
      <h2 class="agreement-title">MANAGED SERVICES AGREEMENT</h2>
      <span class="plan-name" style="left:330px">ESSENTIAL</span>
      <span class="plan-name" style="left:399px">BUSINESS</span>
      <span class="plan-name" style="left:467px">PROFESSIONAL</span>
    </header>

    <div class="section support">
      <div class="section-rail"><span>SUPPORT</span></div>
      <div class="section-rows">
        <div class="row"><div class="feature">Unlimited Remote Support 7am to 6pm</div><div class="cell mark"><svg><use href="#tick"/></svg></div><div class="cell mark"><svg><use href="#tick"/></svg></div><div class="cell mark"><svg><use href="#tick"/></svg></div></div>
        <div class="row"><div class="feature">3<sup style="font-size:7px">rd</sup>&nbsp;Party Vendor Support</div><div class="cell mark"><svg><use href="#tick"/></svg></div><div class="cell mark"><svg><use href="#tick"/></svg></div><div class="cell mark"><svg><use href="#tick"/></svg></div></div>
        <div class="row"><div class="feature">Reactive Onsite Support 8am to 5pm VIP Rates</div><div class="cell">VIP Rates</div><div class="cell mark"><svg><use href="#tick"/></svg></div><div class="cell mark"><svg><use href="#tick"/></svg></div></div>
        <div class="row"><div class="feature">After-Hours Support</div><div class="cell">VIP Rates</div><div class="cell">VIP Rates</div><div class="cell mark"><svg><use href="#tick"/></svg></div></div>
      </div>
    </div>

    <div class="section service">
      <div class="section-rail"><span>SERVICE</span></div>
      <div class="section-rows">
        <div class="row"><div class="feature">Guaranteed SLA Response Times</div><div class="cell mark"><svg><use href="#tick"/></svg></div><div class="cell mark"><svg><use href="#tick"/></svg></div><div class="cell mark"><svg><use href="#tick"/></svg></div></div>
        <div class="row"><div class="feature">24x7 Website &amp; Infrastructure Monitoring</div><div class="cell mark"><svg><use href="#tick"/></svg></div><div class="cell mark"><svg><use href="#tick"/></svg></div><div class="cell mark"><svg><use href="#tick"/></svg></div></div>
        <div class="row"><div class="feature">Secure Web Content Filtering</div><div class="cell mark"><svg><use href="#tick"/></svg></div><div class="cell mark"><svg><use href="#tick"/></svg></div><div class="cell mark"><svg><use href="#tick"/></svg></div></div>
        <div class="row"><div class="feature">Backup Monitoring</div><div class="cell mark"><svg><use href="#tick"/></svg></div><div class="cell mark"><svg><use href="#tick"/></svg></div><div class="cell mark"><svg><use href="#tick"/></svg></div></div>
        <div class="row"><div class="feature">Desktop OS Patching &amp; Updating</div><div class="cell mark"><svg><use href="#tick"/></svg></div><div class="cell mark"><svg><use href="#tick"/></svg></div><div class="cell mark"><svg><use href="#tick"/></svg></div></div>
        <div class="row"><div class="feature">CEO / MD Home Tech Support</div><div class="cell mark"><svg><use href="#tick"/></svg></div><div class="cell mark"><svg><use href="#tick"/></svg></div><div class="cell mark"><svg><use href="#tick"/></svg></div></div>
        <div class="row"><div class="feature">Monthly Tech Site Visit – Quarterly Monthly</div><div class="cell mark"><svg><use href="#cross"/></svg></div><div class="cell">Quarterly</div><div class="cell">Monthly</div></div>
        <div class="row"><div class="feature">Short Term Loan Equipment</div><div class="cell mark"><svg><use href="#cross"/></svg></div><div class="cell">1 Month</div><div class="cell">3 Month</div></div>
        <div class="row"><div class="feature">Adds / Moves / Changes (Staff)</div><div class="cell mark"><svg><use href="#tick"/></svg></div><div class="cell mark"><svg><use href="#tick"/></svg></div><div class="cell mark"><svg><use href="#tick"/></svg></div></div>
        <div class="row"><div class="feature">Adds / Moves / Changes (Workstations)</div><div class="cell">VIP Rates</div><div class="cell">VIP Rates</div><div class="cell mark"><svg><use href="#tick"/></svg></div></div>
      </div>
    </div>

    <div class="section management">
      <div class="section-rail"><span>MANAGEMENT</span></div>
      <div class="section-rows">
        <div class="row"><div class="feature">Asset and Warranty Tracking &amp; Reporting</div><div class="cell mark"><svg><use href="#tick"/></svg></div><div class="cell mark"><svg><use href="#tick"/></svg></div><div class="cell mark"><svg><use href="#tick"/></svg></div></div>
        <div class="row"><div class="feature">Comprehensive IT Documentation</div><div class="cell mark"><svg><use href="#tick"/></svg></div><div class="cell mark"><svg><use href="#tick"/></svg></div><div class="cell mark"><svg><use href="#tick"/></svg></div></div>
        <div class="row"><div class="feature">Technology Strategy Meeting</div><div class="cell">Annual</div><div class="cell">Quarterly</div><div class="cell">Monthly</div></div>
        <div class="row"><div class="feature">Technology Business Review Meeting</div><div class="cell">Annual</div><div class="cell">Bi Annual</div><div class="cell">Quarterly</div></div>
        <div class="row"><div class="feature">IT Policy Templates</div><div class="cell mark"><svg><use href="#cross"/></svg></div><div class="cell mark"><svg><use href="#tick"/></svg></div><div class="cell mark"><svg><use href="#tick"/></svg></div></div>
      </div>
    </div>

    <div class="section training">
      <div class="section-rail"><span>TRAINING</span></div>
      <div class="section-rows">
        <div class="row"><div class="feature">End User Training Materials</div><div class="cell mark"><svg><use href="#cross"/></svg></div><div class="cell mark"><svg><use href="#cross"/></svg></div><div class="cell mark"><svg><use href="#tick"/></svg></div></div>
        <div class="row"><div class="feature">Security Awareness Training</div><div class="cell mark"><svg><use href="#tick"/></svg></div><div class="cell mark"><svg><use href="#tick"/></svg></div><div class="cell mark"><svg><use href="#tick"/></svg></div></div>
      </div>
    </div>
  </section>

  <div class="price-band rrp"><span class="band-label">RRP / User</span><span class="band-value" style="left:296px">$110</span><span class="band-value" style="left:364px">$130</span><span class="band-value" style="left:433px">$165</span></div>
  <div class="price-band users"><span class="band-label">Minimum User Count</span><span class="band-value" style="left:259px">5</span><span class="band-value" style="left:327px">5</span><span class="band-value" style="left:396px">5</span></div>
  <div class="price-band commit"><span class="band-label" style="color:#fff">Minimum Monthly Commit</span><span class="band-value" style="left:218px;color:#fff">$550</span><span class="band-value" style="left:286px;color:#fff">$650</span><span class="band-value" style="left:355px;color:#fff">$825</span></div>

  <p class="version">Version 1.0<br>Updated: April 2024</p>

  <footer class="footer">
    <svg class="footer-art" width="686" height="70" viewBox="0 0 686 70" aria-hidden="true">
      <rect width="686" height="70" fill="var(--charcoal)"/>
      <polygon points="221,0 462,0 430,37 250,37" fill="#fff"/>
      <polygon points="250,37 430,37 462,70 226,70" fill="var(--orange)"/>
    </svg>
    <div class="footer-contact">
      <div><svg viewBox="0 0 10 8"><rect width="10" height="8" fill="var(--orange)"/><path d="M0 0 L5 4.5 L10 0" stroke="#fff" stroke-width="1" fill="none"/></svg>nexwaveit.com.au</div>
      <div><svg viewBox="0 0 10 8"><rect width="10" height="8" fill="var(--orange)"/><path d="M0 0 L5 4.5 L10 0" stroke="#fff" stroke-width="1" fill="none"/></svg>service@nexwaveit.com.au</div>
    </div>
    <div class="company">NEXWAVE IT<br>SERVICES <span style="color:var(--charcoal)">PTY LTD</span></div>
    <div class="abn">ABN: 51 824 753 009</div>
    <div class="footer-call">
      <div class="phone">1300 555 019 <svg viewBox="0 0 12 12"><path d="M2.5 1 L4.5 1 L5.5 3.8 L4.2 5 Q5.3 7 7 7.8 L8.2 6.5 L11 7.5 L11 9.5 Q10 11 8.5 11 Q2 9.5 1 3.5 Q1 2 2.5 1 Z" fill="var(--orange)"/></svg></div>
      <div class="address">12/40 Harbour Lane, Eastfield VIC 3999 <svg viewBox="0 0 11 12"><path d="M5.5 0.5 Q9.5 0.5 9.5 4.5 Q9.5 7 5.5 11.5 Q1.5 7 1.5 4.5 Q1.5 0.5 5.5 0.5 Z" fill="var(--orange)"/><circle cx="5.5" cy="4.5" r="1.6" fill="var(--charcoal)"/></svg></div>
    </div>
  </footer>
</main>
</body>
</html>
```